Business Card Design

No logos or construction designs

Easy to read Ray Tolliver Roofing, LLC (in red)

all other lettering in black I guess I am open to what the designers come up

Industry/Entity Type

Construction

Contact Information for Business Card

Ray Tolliver Roofing, LLC office 555-2189063 fax 555-318-940 3075 Marrowfield W Corvale, Westmark 40000
Ray@RayTolliverRoofing.example Residential Commerical
Ray Tolliver cell 555-862-1375

```html
<!DOCTYPE html>
<html lang="en">
<head>
<meta charset="utf-8">
<title>Ray Tolliver Roofing, LLC – Business Card</title>
<link rel="stylesheet" href="https://fonts.googleapis.com/css2?family=Source+Sans+3:ital,wght@0,400;0,700;1,700&display=swap">
<style>
  :root {
    --backdrop: #ececec;
    --card: #ffffff;
    --brand-red: #a80d14;
    --ink: #3d3d3d;
    --icon: #3a3a3a;
    --on-red: #ffffff;
  }
  * { margin: 0; padding: 0; box-sizing: border-box; }
  html, body {
    width: 1200px;
    height: 1200px;
    overflow: hidden;
    background: var(--backdrop);
  }
  .canvas {
    position: relative;
    width: 1200px;
    height: 1200px;
  }
  .card {
    position: absolute;
    left: 100px;
    top: 314px;
    width: 1000px;
    height: 572px;
    background: var(--card);
    overflow: hidden;
  }
  .company-name {
    position: absolute;
    left: 62px;
    top: 150px;
    font-family: "Source Sans 3", sans-serif;
    font-weight: 700;
    font-size: 62px;
    line-height: 1.0;
    color: var(--brand-red);
  }
  .service-band {
    position: absolute;
    left: 96px;
    right: 0;
    top: 298px;
    height: 46px;
    background: var(--brand-red);
    display: flex;
    align-items: center;
    padding-left: 28px;
    font-family: "Source Sans 3", sans-serif;
    font-size: 26px;
    color: var(--on-red);
    white-space: nowrap;
  }
  .service-band .services { font-weight: 700; font-style: italic; margin-right: 12px; }
  .service-band .owner { font-weight: 700; }
  .service-band .divider { margin: 0 12px; font-weight: 400; }
  .contact-list {
    position: absolute;
    right: 48px;
    top: 366px;
    list-style: none;
    font-family: "Source Sans 3", sans-serif;
    font-size: 24px;
    color: var(--ink);
    text-align: right;
  }
  .contact-list li {
    display: flex;
    justify-content: flex-end;
    align-items: center;
    height: 38px;
    white-space: nowrap;
  }
  .contact-list .icon {
    width: 26px;
    height: 26px;
    margin-left: 12px;
    flex: none;
  }
</style>
</head>
<body>
<div class="canvas">
  <div class="card">
    <h1 class="company-name">Ray Tolliver<br>Roofing, LLC</h1>

    <div class="service-band">
      <span class="services">Residential Commerical</span>
      <span class="owner">Ray Tolliver</span>
      <span class="divider">|</span>
      <span class="cell">555-862-1375</span>
    </div>

    <ul class="contact-list">
      <li>
        <span>555-2189063</span>
        <svg class="icon" viewBox="0 0 26 26" aria-label="Office phone">
          <circle cx="13" cy="13" r="13" fill="var(--icon)"/>
          <path d="M8.5 7.5c1-.8 2-.5 2.5.4l1 1.9c.3.6.1 1.2-.4 1.6l-.7.5c.6 1.5 1.7 2.6 3.2 3.3l.5-.7c.4-.5 1-.7 1.6-.4l1.9 1c.9.5 1.1 1.6.4 2.5-1 1.1-2.6 1.4-4.3.6-2.9-1.4-5.3-3.8-6.4-6.6-.6-1.6-.3-3.1.7-4.1z" fill="#fff"/>
        </svg>
      </li>
      <li>
        <span>555-318-940</span>
        <svg class="icon" viewBox="0 0 26 26" aria-label="Fax">
          <circle cx="13" cy="13" r="13" fill="var(--icon)"/>
          <rect x="9" y="6" width="8" height="5" fill="#fff"/>
          <rect x="6" y="11" width="14" height="7" rx="1.5" fill="#fff"/>
          <rect x="9" y="15" width="8" height="5" fill="#fff" stroke="var(--icon)" stroke-width="1"/>
        </svg>
      </li>
      <li>
        <span>Ray@RayTolliverRoofing.example</span>
        <svg class="icon" viewBox="0 0 26 26" aria-label="Email">
          <circle cx="13" cy="13" r="12" fill="#fff" stroke="var(--icon)" stroke-width="2"/>
          <rect x="6.5" y="8.5" width="13" height="9" fill="none" stroke="var(--icon)" stroke-width="1.5"/>
          <path d="M6.5 8.5l6.5 5 6.5-5" fill="none" stroke="var(--icon)" stroke-width="1.5"/>
        </svg>
      </li>
      <li>
        <span>3075 Marrowfield W Corvale, Westmark 40000</span>
        <svg class="icon" viewBox="0 0 26 26" aria-label="Address">
          <circle cx="13" cy="13" r="13" fill="var(--icon)"/>
          <path d="M13 6l7 6h-2v7h-4v-4h-2v4H8v-7H6z" fill="#fff"/>
        </svg>
      </li>
    </ul>
  </div>
</div>
</body>
</html>
```